vehicle livery flyer

a flyer to go under windscreen wipers solely aimed at van drivers / companies using the vans for advertising thier companies.... ie Van Livery

use company logo , file supplied and be creative

id like this re designed, using different pictures , same logo....in a postcard style.

Livery

```html
<!DOCTYPE html>
<html lang="en">
<head>
<meta charset="utf-8">
<title>KVD Vehicle Livery Flyer</title>
<link rel="stylesheet" href="https://fonts.googleapis.com/css2?family=Arimo:wght@400;700&display=swap">
<style>
  :root {
    --carbon-dark: #17191b;
    --carbon-mid: #2d3033;
    --carbon-light: #3a3d40;
    --headline-yellow: #ffe600;
    --body-white: #f2f2f2;
    --band-teal-dark: #0b3b48;
    --band-teal: #0a7fa3;
    --band-cyan: #1ab4ea;
    --frame-white: #ffffff;
  }
  * { box-sizing: border-box; margin: 0; padding: 0; }
  html, body { width: 1200px; height: 846px; overflow: hidden; }
  body {
    font-family: "Arimo", "Helvetica Neue", Arial, sans-serif;
    background: var(--carbon-dark);
  }
  .flyer {
    position: relative;
    width: 1200px;
    height: 846px;
    background: radial-gradient(ellipse at 50% 20%, var(--carbon-light) 0%, var(--carbon-mid) 40%, var(--carbon-dark) 100%);
    overflow: hidden;
  }
  .intro {
    position: absolute;
    left: 75px;
    top: 66px;
    width: 1053px;
    font-size: 20.5px;
    line-height: 28px;
    text-align: justify;
    color: var(--body-white);
  }
  .intro p + p { margin-top: 28px; }
  .intro .lead {
    color: var(--headline-yellow);
    font-weight: 700;
  }
  .gallery-band {
    position: absolute;
    left: 0;
    top: 403px;
    width: 1200px;
    height: 244px;
    background: linear-gradient(90deg, var(--band-teal-dark) 0%, var(--band-teal) 45%, var(--band-cyan) 100%);
  }
  .gallery-band::before {
    content: "";
    position: absolute;
    left: 0; right: 0; top: 0;
    height: 12px;
    background: linear-gradient(180deg, rgba(0,0,0,0.35), rgba(0,0,0,0));
  }
  .vehicle-photo {
    position: absolute;
    top: 28px;
    width: 244px;
    height: 186px;
    border: 7px solid var(--frame-white);
    box-shadow: 4px 6px 10px rgba(0,0,0,0.45);
  }
  .vehicle-photo.red-van { left: 70px; background: linear-gradient(160deg, #c9d4dc 0%, #b81d24 45%, #7d1015 100%); }
  .vehicle-photo.black-van { left: 341px; background: linear-gradient(150deg, #6a7a88 0%, #f1f1f1 40%, #1b1d22 100%); }
  .vehicle-photo.green-car { left: 612px; background: linear-gradient(165deg, #a7b6ad 0%, #7fb43e 45%, #3f6b24 100%); }
  .vehicle-photo.blue-van { left: 884px; background: linear-gradient(160deg, #c6ccd2 0%, #1d3f8f 50%, #e86b1c 100%); }
  .contact {
    position: absolute;
    left: 0;
    top: 676px;
    width: 1200px;
    text-align: center;
    color: var(--frame-white);
  }
  .contact .phone-email {
    font-size: 62px;
    font-weight: 700;
    line-height: 70px;
    letter-spacing: 0.5px;
  }
  .contact .address {
    font-size: 28px;
    line-height: 34px;
    margin-top: 2px;
  }
</style>
</head>
<body>
  <main class="flyer">
    <section class="intro">
      <p class="lead">Vehicle graphics are one of the most cost-effective ways to raise the profile of your business and how it’s seen. From simple logos and contact details to bright colourful vehicle wraps, KVD can turn your car, sports car, taxi, van, truck or bus into a mobile advertising board.</p>
      <p>So if you are looking for car graphics, vehicle wrapping, signwriting, custom decals, lorry &amp; bus graphic, fleet graphics &amp; promotional vinyl graphics KVD can help.</p>
      <p>Don’t lose the marketing opportunity, display your brand and services to the masses. KVD are Specialists in commercial fleet livery so whether it be 1 or 100 vehicles, KVD leads the field by creating high quality graphics on time and to your budget.</p>
    </section>

    <section class="gallery-band">
      <div class="vehicle-photo red-van" role="img" aria-label="Photo of a red van with a coffee company livery"></div>
      <div class="vehicle-photo black-van" role="img" aria-label="Photo of a black van wrapped with large promotional graphics"></div>
      <div class="vehicle-photo green-car" role="img" aria-label="Photo of a small car in a bright green illustrated wrap"></div>
      <div class="vehicle-photo blue-van" role="img" aria-label="Photo of a blue service van with orange chevron livery"></div>
    </section>

    <footer class="contact">
      <p class="phone-email">020 7946 0321 | info@kvd-ltd.com</p>
      <p class="address">Address: 18 Farrow Lane, Tolworth, Surrey, KT5 9QP</p>
    </footer>
  </main>
</body>
</html>
```